BUSINESS CARD DESIGN

NAME- TODD MASVERIK
PHONE NUMER - 808- 451-7082
EMAIL- OFFICE@VORLINDE-GRADEWAY.COM
BACK OF CARD- SPEACIALIZES IN LAND CLEARING, FORESTRY MUCLHING AND EXCAVATION

Contact Information for Business Card

NAME- TODD MASVERIK PHONE NUMER - 808- 451-7082 EMAIL- OFFICE@VORLINDE-GRADEWAY.COM BACK OF CARD- SPEACIALIZES IN LAND CLEARING , MUCLHING AND EXCAVATION

```html
<!DOCTYPE html>
<html lang="en">
<head>
<meta charset="utf-8">
<title>Business Card – Vorlinde Gradeway</title>
<link href="https://fonts.googleapis.com/css2?family=Montserrat:wght@400;500;700&display=swap" rel="stylesheet">
<style>
  :root {
    --backdrop: #e2e2e2;
    --card-dark: #2a2a2a;
    --card-light: #ffffff;
    --silver: #c9c9c9;
    --tagline-grey: #8c8c8c;
    --ink: #111111;
    --ink-soft: #2b2b2b;
    --muted: #6d6d6d;
    --rule: #555555;
  }
  * { margin: 0; padding: 0; box-sizing: border-box; }
  html, body {
    width: 1200px; height: 1200px; overflow: hidden;
    background: var(--backdrop);
    font-family: "Montserrat", sans-serif;
  }
  .card {
    position: absolute;
    left: 180px;
    width: 867px;
    height: 498px;
  }
  .card--front { top: 85px; background: var(--card-dark); }
  .card--back { top: 625px; background: var(--card-light); }

  /* Front */
  .front-brand {
    position: absolute; left: 0; right: 0; top: 210px;
    display: flex; align-items: center; justify-content: center; gap: 14px;
  }
  .brand-dot {
    width: 22px; height: 22px; border-radius: 50%;
    background: var(--silver);
  }
  .front-brand .brand-name {
    font-weight: 700; font-size: 34px; letter-spacing: 2px;
    color: var(--silver);
  }
  .front-sub {
    position: absolute; left: 0; right: 0; top: 262px;
    text-align: center; font-weight: 500; font-size: 14px;
    letter-spacing: 6px; color: var(--silver);
  }
  .tagline {
    position: absolute; left: 0; right: 0; top: 373px;
    text-align: center; font-size: 21px; line-height: 27px;
    letter-spacing: 1.4px; color: var(--tagline-grey);
  }

  /* Back */
  .back-brand {
    position: absolute; left: 96px; top: 200px;
    display: flex; align-items: center; gap: 10px;
  }
  .back-brand .brand-dot { width: 16px; height: 16px; background: var(--ink); }
  .back-brand .brand-name {
    font-weight: 700; font-size: 21px; letter-spacing: 1px; color: var(--ink);
  }
  .person {
    position: absolute; right: 94px; top: 268px; text-align: right;
  }
  .person-name {
    font-weight: 700; font-size: 30px; letter-spacing: 0.5px;
    color: var(--ink); line-height: 36px;
  }
  .person-role {
    font-size: 20px; letter-spacing: 1.5px; color: var(--muted);
    margin-top: 2px; margin-right: 8px;
  }
  .divider {
    position: absolute; left: 100px; width: 674px; top: 344px;
    height: 1px; background: var(--rule);
  }
  .contact {
    position: absolute; left: 100px; top: 355px; list-style: none;
  }
  .contact li {
    display: flex; align-items: center; gap: 12px;
    font-size: 19px; letter-spacing: 1.3px; color: var(--ink-soft);
    height: 29px;
  }
  .contact svg { width: 20px; height: 20px; fill: var(--ink); }
  .address {
    position: absolute; right: 91px; top: 355px; text-align: right;
    font-size: 19px; line-height: 29px; letter-spacing: 1.8px; color: var(--ink-soft);
    font-style: normal;
  }
</style>
</head>
<body>
  <section class="card card--front">
    <div class="front-brand">
      <span class="brand-dot"></span>
      <span class="brand-name">VORLINDE GRADEWAY</span>
    </div>
    <div class="front-sub">LLC · 808-451-7082</div>
    <p class="tagline">SPEACIALIZES IN LAND CLEARING , MUCLHING<br>AND EXCAVATION</p>
  </section>

  <section class="card card--back">
    <div class="back-brand">
      <span class="brand-dot"></span>
      <span class="brand-name">VORLINDE GRADEWAY</span>
    </div>

    <div class="person">
      <div class="person-name">TODD MASVERIK</div>
      <div class="person-role">DIRECRTOR</div>
    </div>

    <div class="divider"></div>

    <ul class="contact">
      <li>
        <svg viewBox="0 0 24 24" aria-hidden="true"><path d="M6.6 10.8a15.1 15.1 0 0 0 6.6 6.6l2.2-2.2a1 1 0 0 1 1-.25 11.4 11.4 0 0 0 3.6.57 1 1 0 0 1 1 1V20a1 1 0 0 1-1 1A17 17 0 0 1 3 4a1 1 0 0 1 1-1h3.5a1 1 0 0 1 1 1c0 1.25.2 2.45.57 3.6a1 1 0 0 1-.25 1z"/></svg>
        808- 451-7082
      </li>
      <li>
        <svg viewBox="0 0 24 24" aria-hidden="true"><path d="M2 5h20v14H2z M3.5 6.5v.3l8.5 6 8.5-6v-.3z" fill-rule="evenodd"/></svg>
        OFFICE@VORLINDE-GRADEWAY.COM
      </li>
    </ul>

    <address class="address">123 Anywhere St.,<br>Any City, ST 12345</address>
  </section>
</body>
</html>
```